Website for boutique digital agency helping high-tech startups accelerate growth.

We need a website design for a relatively young company based in Mauritius called 'LumaTrel'.

We are a professional services firm delivering digital infrastructure for revenue operations (RevOps)*.

Entrepreneurial startups and SMBs in the technology sector work with us to accelerate growth by delivering extraordinary customer experiences across the full customer lifecycle.

We would like a colourful design that utilises the (4) colours of our existing logo design.

The final design should communicate dynamic growth through relentless customer focus.
----------------------------------------------------------
*Revenue Operations (RevOps) is the strategic alignment of sales, marketing and customer success operations to accelerate growth by delivering extraordinary customer experiences across the full customer life cycle.

Target Market(s)

Entrepreneurial startups and SMBs (Small/Medium Businesses) in the technology sector.

Question: Why the technology sector?

Answer: Because technology entrepreneurs often have a tremendous challenge to effectively communicate to the market and to prospective customers the value and the benefits of their products & services due to the inherent complexity of technological innovation.

LumaTrel is a team of creatively-minded engineers and technologists who have worked with and understand the technologies and innovations our clients are passionate about bringing to market.

Industry/Entity Type

Professional Service

Number of Pages Required

5+ page

Font styles to use
Sans Serif

Requirements
Must have
• Minimalistic designs rich with visual meaning are highly preferred. Mobile responsive designs are also required. Must show how designs render on Desktop, Tablet and Smartphone devices.

Website pages:
1) Homepage: problem statement, target customers, value proposition & benefits
2) Services: 3-4 tiers of services packages with pricing and "how to work with us"
3) Resources: links to all kinds of relevant materials
4) Contact Us: contact form and special project quote form
5) Blog: matrix design with featured images for each post
Nice to have
• Bold, interesting, colourful, inspiring images that visually communicate:
- relentless customer focus
- extraordinary, memorable experiences
- business at the speed of innovation
Should not have
• Any meme or theme that panders to "political correctness".

```html
<!DOCTYPE html>
<html lang="en">
<head>
<meta charset="utf-8">
<title>LumaTrel — Digital Agency</title>
<link href="https://fonts.googleapis.com/css2?family=Poppins:wght@400;500;600;700&display=swap" rel="stylesheet">
<style>
:root{
  --teal:#157d82;
  --green:#7cc21b;
  --red:#f5112e;
  --orange:#fb6a10;
  --ink:#141a2b;
  --body:#3a3f4d;
  --soft:#eff2fb;
  --line:#dde0ea;
  --footer:#1e1f22;
  --footer-text:#d9dbe0;
  --white:#ffffff;
}
*{margin:0;padding:0;box-sizing:border-box}
html,body{width:1200px;height:2766px;overflow:hidden}
body{position:relative;font-family:'Poppins',sans-serif;color:var(--body);background:var(--white)}
a{text-decoration:none}
.abs{position:absolute}

/* hero */
.hero{left:0;top:0;width:1200px;height:585px;background:linear-gradient(100deg,#147c81 0%,#1b8a8f 55%,#2a8e92 75%,#147a80 100%)}
.wave{left:0;top:470px;width:1200px;height:120px}
.brand{left:235px;top:21px;display:flex;flex-direction:column;align-items:flex-start;gap:8px}
.brand-mark{width:44px;height:44px;border-radius:50%;background:var(--white);margin-left:45px}
.brand-name{font-weight:700;font-size:26px;color:var(--white);line-height:1}
.nav{left:457px;top:61px;display:flex;gap:25px}
.nav a{color:var(--white);font-size:10.5px;font-weight:500;letter-spacing:.2px}
.call{left:819px;top:52px;display:flex;align-items:center;gap:10px;color:var(--white)}
.call small{display:block;font-size:9.5px;font-weight:500}
.call strong{display:block;font-size:16px;font-weight:600;line-height:1.1}
.hero-title{left:0;width:1200px;top:172px;text-align:center;color:var(--white);font-weight:700;font-size:47px;line-height:53px}
.hero-sub{left:0;width:1200px;top:284px;text-align:center;color:var(--white);font-size:16.5px;line-height:24px}
.play{left:542px;top:349px;width:114px;height:114px;border-radius:50%;background:rgba(255,255,255,.18);display:flex;align-items:center;justify-content:center}
.play span{width:92px;height:92px;border-radius:50%;background:linear-gradient(135deg,var(--orange),var(--red));display:flex;align-items:center;justify-content:center}

/* shared type */
.eyebrow{font-size:9.5px;font-weight:500;color:var(--green);text-transform:uppercase;line-height:14px}
.h2{font-weight:600;color:var(--ink);font-size:21px;line-height:30px}
.copy{font-size:10.6px;line-height:17.6px;color:var(--body)}
.copy + .copy{margin-top:17px}
.btn{display:flex;align-items:center;justify-content:center;background:linear-gradient(90deg,var(--red),var(--orange));color:var(--white);font-weight:600;font-size:10px;text-transform:uppercase}

/* about */
.about-photo{left:234px;top:657px;width:294px;height:413px;background:linear-gradient(160deg,#c9765a,#e9d3c4 45%,#5c6f86);box-shadow:0 4px 10px rgba(0,0,0,.15)}
.about-text{left:546px;top:655px;width:420px}
.about-text .h2{margin-top:2px}
.about-text .copy:first-of-type{margin-top:14px}
.about-text .btn{margin-top:24px;width:126px;height:40px}

/* target */
.band{left:0;top:1138px;width:1200px;height:442px;background:var(--soft)}
.target-text{left:233px;top:1200px;width:315px}
.target-text .h2{margin-bottom:12px}
.target-art{left:580px;top:1180px;width:386px;height:356px;border-radius:12px;background:linear-gradient(135deg,#dfe7f8 0%,#f3e4e8 100%)}

/* values */
.card{width:232px;height:215px;background:var(--soft);text-align:center}
.card-icon{position:absolute;left:86px;top:-27px;width:60px;height:60px;border-radius:50%;border:3px solid var(--white);display:flex;align-items:center;justify-content:center}
.card h3{position:absolute;top:58px;left:0;width:100%;font-size:14.5px;font-weight:600;color:var(--ink)}
.card p{position:absolute;top:86px;left:18px;width:196px;font-size:10.4px;line-height:17.6px}

/* news */
.post{width:231px}
.post-img{width:231px;height:149px}
.post-title{margin-top:16px;font-size:13px;font-weight:600;color:var(--ink);line-height:15.5px}
.meta{font-size:9px;color:var(--body);line-height:12px}
.post .meta{margin-top:9px}
.excerpt{margin-top:8px;font-size:9.2px;line-height:15.5px}
.post-rule{margin-top:8px;height:1px;background:var(--line)}
.more{display:block;margin-top:13px;font-size:9.6px;color:var(--ink)}
.side-list{left:734px;top:2086px;width:232px;height:282px;border:1px solid var(--line)}
.side-item{height:94px;border-bottom:1px solid var(--line);padding:22px 18px 0 19px}
.side-item:last-child{border-bottom:none}
.side-item h4{font-size:11.8px;font-weight:600;color:var(--ink);line-height:14px}
.side-item .meta{margin-top:14px}

/* footer */
.footer{left:0;top:2434px;width:1200px;height:332px;background:var(--footer)}
.f-head{font-size:11px;font-weight:600;color:var(--white);text-transform:uppercase}
.f-line{width:28px;height:2px;background:var(--green)}
.f-list{list-style:none;font-size:9.2px;color:var(--footer-text)}
.f-list li{height:22.5px;display:flex;align-items:center;gap:8px}
.f-list .chev{color:var(--green);font-size:10px}
.input{left:734px;top:2565px;width:232px;height:33px;border:1px solid var(--footer-text);color:var(--footer-text);font-size:9.4px;padding:0 12px;display:flex;align-items:center}
.social{width:26px;height:26px;border-radius:50%;border:1.5px solid var(--white)}
</style>
</head>
<body>

<header>
  <div class="abs hero" role="img" aria-label="Teal-tinted photo of a smiling businesswoman in an office"></div>
  <svg class="abs wave" viewBox="0 0 1200 120" preserveAspectRatio="none" aria-hidden="true">
    <path d="M0 32 C 90 70,170 86,260 80 C 360 72,420 60,500 40 C 560 26,620 30,660 46 C 740 78,820 60,900 34 C 980 12,1080 28,1200 0 L1200 120 L0 120 Z" fill="#ffffff"/>
  </svg>

  <div class="abs brand">
    <span class="brand-mark"></span>
    <span class="brand-name">lumatrel.io</span>
  </div>

  <nav class="abs nav">
    <a href="#">HOME</a><a href="#">SERVICES</a><a href="#">RESOURCES</a><a href="#">BLOG</a><a href="#">CONTACT US</a>
  </nav>

  <div class="abs call">
    <svg width="22" height="22" viewBox="0 0 24 24" aria-hidden="true"><circle cx="12" cy="12" r="10.5" fill="none" stroke="#fff" stroke-width="1.5"/><path d="M8.5 7l2 2-1.2 1.5c.7 1.6 2 2.9 3.6 3.6L14.4 13l2 2-1.2 1.5C11.8 16.3 7.7 12.2 7.5 8.8z" fill="#fff"/></svg>
    <div><small>CALL US</small><strong>(000) 555 0142</strong></div>
  </div>

  <h1 class="abs hero-title">Grow Your Business<br>&amp; Make More Profit</h1>
  <p class="abs hero-sub">Lorem ipsum dolor sit amet, consectetur adipiscing elit. Sed egestas<br>placerat lacus, eget tristique nisi lacinia gravida.</p>
  <div class="abs play"><span><svg width="16" height="16" viewBox="0 0 16 16" aria-hidden="true"><path d="M4 2l10 6-10 6z" fill="#fff"/></svg></span></div>
</header>

<section class="about">
  <div class="abs about-photo" role="img" aria-label="Photo of three happy colleagues looking at a laptop"></div>
  <div class="abs about-text">
    <p class="eyebrow">Who we are</p>
    <h2 class="h2">We are full fledged Digital Agency<br>Having 10 years Successful Expericences.</h2>
    <p class="copy">Lorem ipsum dolor sit amet, consectetur adipiscing elit. Sed egestas placerat lacus, eget tristique nisi lacinia gravida. Fusce eu aliquam nisl. Nunc ac nisi nec quam finibus volutpat. Mauris ac nisi sapien. In blandit rhoncus auctor. Sed at lectus dictum, semper quam ac, dignissim dolor. Sed in est vel leo elementum tincidunt. Praesent at condimentum metus. Maecenas bibendum ultrices ligula vel ullamcorper.</p>
    <p class="copy">Mauris sit amet risus hendrerit, lobortis nisl ut, congue ante. Nulla aliquet diam id leo sollicitudin faucibus. Mauris consectetur justo vitae leo ultrices efficitur. Fusce odio eros, ullamcorper vel leo eget, rhoncus vulputate risus. Pellentesque porttitor dui massa, porta posuere ex rhoncus vel. Fusce ut leo a massa vestibulum sagittis sed ac urna. Pellentesque dictum efficitur felis, sed tincidunt erat ullamcorper ut. Nulla sed ligula dolor.</p>
    <a class="btn" href="#">Our Services</a>
  </div>
</section>

<section class="target">
  <div class="abs band"></div>
  <div class="abs target-text">
    <h2 class="h2">Target Customers</h2>
    <p class="copy">Lorem ipsum dolor sit amet, consectetur adipiscing elit. Sed egestas placerat lacus, eget tristique nisi lacinia gravida. Fusce eu aliquam nisl. Nunc ac nisi nec quam finibus volutpat. Mauris ac nisi sapien. In blandit rhoncus auctor. Sed at lectus dictum, semper quam ac, dignissim dolor. Sed in est vel leo elementum tincidunt. Praesent at condimentum metus. Maecenas bibendum ultrices ligula vel ullamcorper.</p>
    <p class="copy">Mauris sit amet risus hendrerit, lobortis nisl ut, congue ante. Nulla aliquet diam id leo sollicitudin faucibus. Mauris consectetur justo vitae leo ultrices efficitur. Fusce odio eros, ullamcorper vel leo eget, rhoncus vulputate risus. Pellentesque porttitor dui massa, porta posuere ex rhoncus vel. Fusce ut leo a massa vestibulum sagittis sed ac urna. Pellentesque dictum efficitur felis, sed tincidunt erat ullamcorper ut. Nulla sed ligula dolor.</p>
  </div>
  <div class="abs target-art" role="img" aria-label="Illustration of a target with an arrow surrounded by customer avatars and icons"></div>
</section>

<section class="values">
  <p class="abs eyebrow" style="left:0;width:1200px;top:1644px;text-align:center">Why choose us</p>
  <h2 class="abs h2" style="left:0;width:1200px;top:1659px;text-align:center">Value Proposition &amp; Benefits</h2>

  <article class="abs card" style="left:234px;top:1743px">
    <div class="card-icon" style="background:var(--green)"><svg width="26" height="20" viewBox="0 0 26 20" aria-hidden="true"><rect x="1" y="1" width="24" height="18" fill="none" stroke="#fff" stroke-width="1.5"/><path d="M1 1l12 10L25 1" fill="none" stroke="#fff" stroke-width="1.5"/></svg></div>
    <h3>Our Responsibility</h3>
    <p>Lorem ipsum dolor sit amet, consec tetur adipisicing elit, sed do eiusmod tempor incididunt ut labore et dolore magna aliqua. Ut enim ad minim veniam, quis nostrud exer citation ullamco laboris.</p>
  </article>
  <article class="abs card" style="left:485px;top:1743px">
    <div class="card-icon" style="background:var(--red)"><svg width="20" height="24" viewBox="0 0 20 24" aria-hidden="true"><rect x="1" y="2" width="18" height="21" fill="none" stroke="#fff" stroke-width="1.5"/><path d="M5 8h10M5 12h10M5 16h10" stroke="#fff" stroke-width="1.5"/></svg></div>
    <h3>Our Approach</h3>
    <p>Lorem ipsum dolor sit amet, consec tetur adipisicing elit, sed do eiusmod tempor incididunt ut labore et dolore magna aliqua. Ut enim ad minim veniam, quis nostrud exer citation ullamco laboris.</p>
  </article>
  <article class="abs card" style="left:735px;top:1743px">
    <div class="card-icon" style="background:var(--orange)"><svg width="24" height="26" viewBox="0 0 24 26" aria-hidden="true"><circle cx="12" cy="11" r="7" fill="none" stroke="#fff" stroke-width="1.5"/><path d="M9 20h6M10 23h4" stroke="#fff" stroke-width="1.5"/></svg></div>
    <h3>Our Mission, Vission</h3>
    <p>Lorem ipsum dolor sit amet, consec tetur adipisicing elit, sed do eiusmod tempor incididunt ut labore et dolore magna aliqua. Ut enim ad minim veniam, quis nostrud exer citation ullamco laboris.</p>
  </article>
</section>

<section class="news">
  <p class="abs eyebrow" style="left:0;width:1200px;top:2020px;text-align:center">Blog</p>
  <h2 class="abs h2" style="left:0;width:1200px;top:2035px;text-align:center">Latest News</h2>

  <article class="abs post" style="left:235px;top:2086px">
    <div class="post-img" style="background:linear-gradient(160deg,#6b6258,#c9b59c 55%,#3d3a36)" role="img" aria-label="Photo of a team working at laptops on a wooden table"></div>
    <h3 class="post-title">Lorem ipsum dolor sit amet, consectetur adipiscing elit.</h3>
    <p class="meta">admin &nbsp;|&nbsp; 02 April 20</p>
    <p class="excerpt">Vivamus sem diam, consequat eu eros in, pellentesque maximus odio. Ut nisi purus, sagittis.</p>
    <div class="post-rule"></div>
    <a class="more" href="#">Read More</a>
  </article>

  <article class="abs post" style="left:485px;top:2086px">
    <div class="post-img" style="background:linear-gradient(160deg,#e8e8e6,#b7a898 50%,#4a4038)" role="img" aria-label="Photo of two businessmen in a meeting"></div>
    <h3 class="post-title">Lorem ipsum dolor sit amet, consectetur adipiscing elit.</h3>
    <p class="meta">admin &nbsp;|&nbsp; 02 April 20</p>
    <p class="excerpt">Vivamus sem diam, consequat eu eros in, pellentesque maximus odio. Ut nisi purus, sagittis.</p>
    <div class="post-rule"></div>
    <a class="more" href="#">Read More</a>
  </article>

  <div class="abs side-list">
    <div class="side-item"><h4>Lorem ipsum dolor sit amet, consectetur adipiscing elit.</h4><p class="meta">admin &nbsp;|&nbsp; 02 April 20</p></div>
    <div class="side-item"><h4>Lorem ipsum dolor sit amet, consectetur adipiscing elit.</h4><p class="meta">admin &nbsp;|&nbsp; 02 April 20</p></div>
    <div class="side-item"><h4>Lorem ipsum dolor sit amet, consectetur adipiscing elit.</h4><p class="meta">admin &nbsp;|&nbsp; 02 April 20</p></div>
  </div>
</section>

<footer>
  <div class="abs footer"></div>

  <h4 class="abs f-head" style="left:235px;top:2482px">Contact Info</h4>
  <div class="abs f-line" style="left:235px;top:2506px"></div>
  <ul class="abs f-list" style="left:234px;top:2529px">
    <li><svg width="9" height="9" viewBox="0 0 10 10" aria-hidden="true"><path d="M1 1l3 0 1 2.5-1.5 1c.6 1.2 1.4 2 2.5 2.5l1-1.5L9.5 6v3C4.5 9 1 5.5 1 1z" fill="#7cc21b"/></svg>+00 5550 1427</li>
    <li><svg width="9" height="8" viewBox="0 0 10 8" aria-hidden="true"><rect width="10" height="8" fill="#7cc21b"/><path d="M0 0l5 4 5-4" fill="none" stroke="#1e1f22" stroke-width="1"/></svg>hello@lumatrel.io</li>
  </ul>
  <a class="abs btn" href="#" style="left:234px;top:2591px;width:185px;height:30px;text-transform:none;font-size:9px">Schedule FREE Consultation Call</a>

  <h4 class="abs f-head" style="left:466px;top:2482px">Quick Links</h4>
  <div class="abs f-line" style="left:466px;top:2506px"></div>
  <ul class="abs f-list" style="left:466px;top:2529px">
    <li><span class="chev">›</span>Home</li><li><span class="chev">›</span>Services</li><li><span class="chev">›</span>Resources</li><li><span class="chev">›</span>Blog</li><li><span class="chev">›</span>Contact Us</li>
  </ul>

  <h4 class="abs f-head" style="left:605px;top:2482px">About</h4>
  <div class="abs f-line" style="left:605px;top:2506px"></div>
  <ul class="abs f-list" style="left:605px;top:2529px">
    <li><span class="chev">›</span>FAQ</li><li><span class="chev">›</span>Our Leadership</li><li><span class="chev">›</span>Careers</li><li><span class="chev">›</span>Terms of Service</li><li><span class="chev">›</span>Privacy</li>
  </ul>

  <h4 class="abs f-head" style="left:734px;top:2482px">Newsletter</h4>
  <div class="abs f-line" style="left:734px;top:2506px"></div>
  <p class="abs" style="left:734px;top:2533px;font-size:9.2px;color:var(--footer-text)">Get monthly market insights and investment ideas</p>
  <div class="abs input">Your email address</div>
  <a class="abs btn" href="#" style="left:735px;top:2610px;width:231px;height:31px;font-size:11px">Subscribe</a>

  <div class="abs" style="left:234px;top:2687px;width:732px;height:1px;background:#3a3b40"></div>
  <p class="abs" style="left:235px;top:2720px;font-size:9px;color:var(--footer-text)">Copyright © 2020 lumatrel.io. All rights reserved.</p>
  <p class="abs" style="left:775px;top:2718px;font-size:10px;font-weight:600;color:var(--white)">FOLLOW US</p>
  <span class="abs social" style="left:844px;top:2711px"></span>
  <span class="abs social" style="left:876px;top:2711px"></span>
  <span class="abs social" style="left:908px;top:2711px"></span>
  <span class="abs social" style="left:939px;top:2711px"></span>
</footer>

</body>
</html>
```